New Mechanical Maintenance business needs website

New Mechanical Maintenance business in Perth Western Australia needs a nice and easy to navigate website. Showing what we do and how we can be the right fit for other small to medium size business by offering personalized service from our highly skilled team. We deal with both fixed plant repairs like food and chemical processing facilities to heavy equipment like drill rigs, Large boats and earthmoving equipment.

Target Market(s)

Small to medium business to offer personalized services/packages

Industry/Entity Type

e deal with both fixed plant repairs like food and chemical processing facilities to heavy equipment like drill rigs, Large boats and earthmoving equipment.

Coding

Coded - Design and coding required

Number of Pages Required

4 page

Font styles to use
Serif

Colors
0054AA
0677BA
7BADD7
CADEEF
E8F1F8

Requirements
Must have
• A website that is easy to navigate but covers off on the range of services/maintenance we can provide

```html
<!DOCTYPE html>
<html lang="en">
<head>
<meta charset="utf-8">
<title>Ridgeway Maintenance</title>
<link href="https://fonts.googleapis.com/css2?family=Rubik:wght@400;500;600;700;800&display=swap" rel="stylesheet">
<style>
:root{
  --navy:#1f3f95;
  --navy-dark:#0e1d47;
  --accent:#0677ba;
  --sky:#7badd7;
  --mist:#cadeef;
  --panel:#e8f1f8;
  --ink:#1b1b1b;
  --grey:#555b63;
  --white:#ffffff;
}
*{box-sizing:border-box;margin:0;padding:0}
html,body{width:1200px;height:3639px;overflow:hidden}
body{position:relative;background:var(--white);font-family:"Rubik",sans-serif;color:var(--ink)}
.abs{position:absolute}
.btn{position:absolute;display:flex;align-items:center;justify-content:center;font-size:11px;font-weight:500;color:var(--white);background:var(--grey);border-radius:3px;letter-spacing:.3px;text-transform:uppercase}
.section-title{position:absolute;left:0;width:1200px;text-align:center;font-size:29px;font-weight:700;color:var(--navy)}
.section-sub{position:absolute;left:0;width:1200px;text-align:center;font-size:12px;color:#333;text-transform:uppercase;letter-spacing:.2px}

/* header */
.topbar{position:absolute;left:0;top:25px;width:1200px;height:55px;background:rgba(255,255,255,.9)}
.brand-badge{position:absolute;left:156px;top:-2px;width:112px;height:112px;border-radius:50%;background:var(--white);border:5px solid #6b6f76;display:flex;align-items:center;justify-content:center}
.brand-badge span{font-size:16px;font-weight:700;color:#4d5158;letter-spacing:1px}
.nav a{position:absolute;top:46px;font-size:12px;color:#222;text-decoration:none}
.nav a.active{color:var(--accent)}
.nav-underline{position:absolute;left:434px;top:78px;width:44px;height:3px;background:var(--accent)}
.social span{position:absolute;width:20px;height:20px;border-radius:50%;border:1.5px solid #777}
.social .on{background:var(--accent);border-color:var(--accent);width:24px;height:24px}
.quote-btn{left:909px;top:37px;width:141px;height:32px;background:var(--accent);font-size:11px;font-weight:600;border-radius:2px}

/* hero */
.hero-title{position:absolute;left:200px;top:176px;font-size:42px;line-height:45px;font-weight:800;color:var(--white);letter-spacing:1px}
.hero-sub{position:absolute;left:200px;top:321px;font-size:12.5px;line-height:20px;font-weight:500;color:var(--white)}

/* about */
.about-frame{position:absolute;left:200px;top:678px;width:167px;height:300px;border:3px solid var(--navy);border-right:none;border-radius:10px 0 0 10px}
.about-photo{position:absolute;left:212px;top:642px;width:339px;height:327px;border-radius:12px;background:linear-gradient(135deg,#2f4a5c 0%,#7a5a3c 45%,#d97a2a 65%,#3b3a3c 100%)}
.exp-badge{position:absolute;left:486px;top:809px;width:107px;height:95px;background:var(--navy);border:3px solid var(--white);border-radius:8px;color:var(--white);text-align:center;padding-top:12px;box-shadow:0 0 0 2px var(--navy)}
.exp-badge b{display:block;font-size:28px;line-height:28px;font-weight:700}
.exp-badge i{display:block;font-style:normal;font-size:13px;font-weight:600;margin-top:4px}
.exp-badge small{display:block;font-size:9px;letter-spacing:.5px}
.about-title{position:absolute;left:659px;top:678px;font-size:29px;font-weight:700;color:var(--navy)}
.about-lead{position:absolute;left:659px;top:728px;width:345px;font-size:12px;line-height:17.5px;font-weight:500}
.about-body{position:absolute;left:659px;top:800px;width:345px;font-size:10.5px;line-height:17.5px;color:#333}

/* services */
.panel{position:absolute;left:150px;width:900px;background:var(--panel);border-radius:14px}
.card{position:absolute;top:1225px;width:252px;height:243px;background:var(--white);box-shadow:0 4px 14px rgba(0,0,0,.06);text-align:center}
.card.featured{background:var(--navy);color:var(--white)}
.card svg.icon{position:absolute;left:94px;top:38px}
.card h3{position:absolute;top:130px;left:0;width:100%;font-size:13.5px;line-height:19px;font-weight:500;text-transform:uppercase}
.card .arrow{position:absolute;left:108px;top:198px;width:36px;height:22px;border-bottom:1px solid currentColor;font-size:16px;line-height:16px}
.slider-line{position:absolute;left:381px;width:438px;height:1px;background:#b9c2cc}
.slider-dot{position:absolute;width:16px;height:16px;border-radius:50%;background:var(--navy)}

/* gallery */
.gallery-item{position:absolute;top:1746px;height:273px}

/* testimonials */
.testi{position:absolute;top:2382px;width:487px;height:252px;background:var(--white);box-shadow:0 4px 14px rgba(0,0,0,.05);text-align:center}
.testi .q{position:absolute;left:220px;top:30px;width:46px;height:46px;border-radius:50%;background:var(--navy);color:var(--white);font-size:34px;font-weight:700;line-height:54px}
.testi p{position:absolute;left:50px;top:102px;width:387px;font-size:10.8px;line-height:16px;color:#222}
.testi .author{position:absolute;left:144px;top:182px;display:flex;align-items:center;text-align:left}
.testi .avatar{width:42px;height:42px;border-radius:50%;background:linear-gradient(#9aa3ad,#4e5661);border:2px solid #ddd;margin-right:7px}
.testi .author b{display:block;font-size:11px;font-weight:600;color:var(--navy)}
.testi .author small{display:block;font-size:9.5px;color:#555}
.dots span{position:absolute;top:2672px;width:8px;height:8px;border-radius:50%;background:var(--navy)}

/* stats */
.stat{position:absolute;top:2831px;width:200px;text-align:center}
.stat .ring{width:70px;height:70px;margin:0 auto;border-radius:50%;background:var(--accent);display:flex;align-items:center;justify-content:center}
.stat b{display:block;margin-top:10px;font-size:21px;font-weight:600}
.stat small{display:block;font-size:11px;text-transform:uppercase}

/* contact */
.contact-card{position:absolute;left:250px;top:3024px;width:702px;height:318px;background:var(--white);box-shadow:0 4px 20px rgba(0,0,0,.12);border-radius:4px}
.contact-photo{position:absolute;left:256px;top:3031px;width:386px;height:302px;background:linear-gradient(135deg,#2c4b6e 0%,#5f7a8c 40%,#c9a34a 60%,#35465a 100%)}
.form-title{position:absolute;left:678px;top:3052px;font-size:18px;font-weight:600;color:var(--navy)}
.field{position:absolute;left:679px;width:234px;height:30px;border:1px solid #d9dde2;border-radius:2px;font-size:10px;color:#999;padding:8px 0 0 24px}
.field svg{position:absolute;left:8px;top:9px}

/* footer */
.footer-brand{position:absolute;left:151px;top:3416px;width:116px;height:116px;border-radius:50%;border:5px solid #d8dde5;display:flex;align-items:center;justify-content:center}
.footer-brand span{font-size:16px;font-weight:700;color:#d8dde5;letter-spacing:1px}
.f-title{position:absolute;top:3402px;font-size:14px;font-weight:500;color:var(--sky)}
.f-text{position:absolute;font-size:11px;line-height:15px;color:var(--white)}
.f-link{position:absolute;left:604px;font-size:11px;color:var(--white)}
.map{position:absolute;left:785px;top:3403px;width:265px;height:139px;background:linear-gradient(135deg,#eef1f4,#dfe5ea);border:3px solid var(--white)}
.bottom-bar{position:absolute;left:0;top:3597px;width:1200px;height:42px;background:var(--navy)}
.bottom-bar p{position:absolute;left:151px;top:14px;font-size:11px;color:var(--white)}
.bottom-bar span{position:absolute;top:13px;width:14px;height:14px;border-radius:50%;border:1.5px solid var(--white)}
</style>
</head>
<body>

<!-- hero -->
<svg class="abs" style="left:0;top:0" width="1200" height="580" viewBox="0 0 1200 580" role="img" aria-label="Smiling technician in hard hat and overalls giving a thumbs up inside a factory">
  <defs>
    <linearGradient id="heroPhoto" x1="0" y1="0" x2="1" y2="0.3">
      <stop offset="0" stop-color="#1b2a44"/>
      <stop offset=".45" stop-color="#3a4a66"/>
      <stop offset=".7" stop-color="#8a8d8f"/>
      <stop offset="1" stop-color="#4a5565"/>
    </linearGradient>
    <linearGradient id="heroBand" x1="0" y1="0" x2="1" y2="0">
      <stop offset="0" stop-color="#0054aa"/>
      <stop offset=".5" stop-color="#1f3f95"/>
      <stop offset="1" stop-color="#0677ba"/>
    </linearGradient>
  </defs>
  <path d="M0 440 C420 625 880 600 1200 432 V0 H0 Z" fill="url(#heroBand)"/>
  <path d="M0 0 H1200 V428 C880 560 420 560 0 440 Z" fill="url(#heroPhoto)"/>
</svg>

<header>
  <div class="topbar"></div>
  <div class="brand-badge"><span>RIDGEWAY</span></div>
  <nav class="nav">
    <a class="active" style="left:439px">Home</a>
    <a style="left:492px">About Us</a>
    <a style="left:563px">What We Do</a>
    <a style="left:648px">Gallery</a>
    <a style="left:707px">Contact Us</a>
  </nav>
  <div class="nav-underline"></div>
  <div class="social">
    <span style="left:798px;top:44px;border:none"><svg width="20" height="20"><circle cx="10" cy="10" r="4" fill="#666"/></svg></span>
    <span class="on" style="left:825px;top:42px"></span>
    <span style="left:857px;top:44px;border:none"><svg width="20" height="20"><rect x="6" y="6" width="8" height="8" fill="#666"/></svg></span>
  </div>
  <div class="btn quote-btn">Request a Quote</div>
</header>

<h1 class="hero-title">WE OFFER<br>PERSONALISED<br>SERVICE</h1>
<p class="hero-sub">TO ALL SMALL AND MEDIUM SIZE BUSINESS ACROSS<br>A DIVERSE RANGE OF INDUSTRIES.</p>
<div class="btn" style="left:200px;top:381px;width:109px;height:30px">Contact Us</div>

<!-- about -->
<div class="about-frame"></div>
<div class="about-photo" role="img" aria-label="Welder in protective mask working with sparks in an industrial plant"></div>
<div class="exp-badge"><b>20+</b><i>YEARS OF</i><small>EXPERIENCE</small></div>
<h2 class="about-title">About Us</h2>
<p class="about-lead">Director of the company has over 20-year experience in the fixed and mobile plant industries ranging from Perth local and overseas.</p>
<p class="about-body">Lorem Ipsum is simply dummy text of the printing and typesetting industry. Lorem Ipsum has been the industry's standard dummy text ever since the 1500s, when an unknown printer took a galley of type and scrambled it to make a type specimen book.</p>
<div class="btn" style="left:659px;top:895px;width:102px;height:31px">Read More</div>

<!-- services -->
<div class="panel" style="top:1056px;height:548px"></div>
<h2 class="section-title" style="top:1122px">What We Do</h2>
<p class="section-sub" style="top:1169px">Provide awesome services for industrial company</p>

<div class="card" style="left:38px;color:var(--ink)">
  <svg class="icon" width="64" height="64" viewBox="0 0 64 64" fill="none" stroke="#1f3f95" stroke-width="2.2"><path d="M10 56h40M16 56v-8h28v8"/><path d="M24 48c0-8 10-10 12-18"/><ellipse cx="44" cy="16" rx="12" ry="8"/><path d="M32 16v8c0 4 24 4 24 0v-8"/></svg>
  <h3>Precious<br>Metals Refining</h3><div class="arrow">→</div>
</div>
<div class="card" style="left:328px;color:var(--ink)">
  <svg class="icon" width="64" height="64" viewBox="0 0 64 64" fill="none" stroke="#1f3f95" stroke-width="2.2"><path d="M8 40h48l-6 10H14z"/><path d="M18 40V22h20v18M28 22V8M44 40V20l6 -8"/><path d="M6 56c6-4 10 4 16 0s10 4 16 0 10 4 20 0"/></svg>
  <h3>Offshore Drilling &amp;<br>Production Platform</h3><div class="arrow">→</div>
</div>
<div class="card featured" style="left:618px">
  <svg class="icon" width="64" height="64" viewBox="0 0 64 64" fill="none" stroke="#ffffff" stroke-width="2.2"><path d="M10 14l26 30M6 22c6-10 16-14 24-12"/><path d="M30 56l20-22 8 22z"/></svg>
  <h3>Open Cut &amp;<br>Underground Mining</h3><div class="arrow">→</div>
</div>
<div class="card" style="left:909px;color:var(--ink)">
  <svg class="icon" width="64" height="64" viewBox="0 0 64 64" fill="none" stroke="#1f3f95" stroke-width="2.2"><path d="M10 58V10h30M40 10l14 6M20 10v12"/><rect x="26" y="24" width="26" height="34"/><path d="M32 32h4M42 32h4M32 42h4M42 42h4M36 58v-8h6v8M6 58h52"/></svg>
  <h3>Construction<br>As an Expat Overseas</h3><div class="arrow">→</div>
</div>
<div class="slider-line" style="top:1521px"></div>
<div class="slider-dot" style="left:555px;top:1513px"></div>

<!-- gallery -->
<h2 class="section-title" style="top:1671px">Gallery</h2>
<div class="gallery-item" style="left:13px;width:274px;background:linear-gradient(160deg,#8d8fa6,#4a4a52 60%,#2b2b30)" role="img" aria-label="Oil refinery towers and pipework at dusk"></div>
<div class="gallery-item" style="left:299px;width:276px;background:linear-gradient(180deg,#3f7fc7 0%,#8ab6de 45%,#c49a2a 62%,#1d5aa0 100%)" role="img" aria-label="Offshore drilling platform at sea"></div>
<div class="gallery-item" style="left:587px;top:1727px;width:314px;height:312px;background:linear-gradient(180deg,#3b4f6b 0%,#c77a40 50%,#5a3420 100%)" role="img" aria-label="Building under construction with scaffolding at sunset">
  <svg class="abs" style="left:145px;top:144px" width="24" height="24"><path d="M12 0v24M0 12h24" stroke="#fff" stroke-width="2"/></svg>
</div>
<div class="gallery-item" style="left:912px;width:275px;background:linear-gradient(135deg,#c95b2a 0%,#36465e 45%,#8fb4d6 100%)" role="img" aria-label="Two engineers reviewing a digital robotics display"></div>
<div class="slider-line" style="top:2078px"></div>
<div class="slider-dot" style="left:555px;top:2070px"></div>
<div class="btn" style="left:556px;top:2113px;width:88px;height:30px">View All</div>

<!-- testimonials -->
<div class="panel" style="top:2219px;height:535px"></div>
<h2 class="section-title" style="top:2285px">Testimonials</h2>
<p class="section-sub" style="top:2332px">What our people say</p>
<div class="testi" style="left:100px">
  <div class="q">“</div>
  <p>Lorem Ipsum is simply dummy text of the printing and typesetting industry. Lorem Ipsum has been the industry's standard dummy text ever since the 1500s, when an unknown printer took a galley of type and scrambled it to make a type specimen book.</p>
  <div class="author"><div class="avatar" role="img" aria-label="Client portrait"></div><div><b>Liam R.</b><small>CEO, Northline Holdings</small></div></div>
</div>
<div class="testi" style="left:613px">
  <div class="q">“</div>
  <p>Lorem Ipsum is simply dummy text of the printing and typesetting industry. Lorem Ipsum has been the industry's standard dummy text ever since the 1500s, when an unknown printer took a galley of type and scrambled it to make a type specimen book.</p>
  <div class="author"><div class="avatar" role="img" aria-label="Client portrait"></div><div><b>Liam R.</b><small>CEO, Northline Holdings</small></div></div>
</div>
<div class="dots">
  <span style="left:570px"></span><span style="left:586px"></span>
  <span style="left:600px;width:16px;border-radius:4px"></span><span style="left:622px"></span>
</div>

<!-- stats -->
<div class="stat" style="left:203px"><div class="ring"><svg width="34" height="34" viewBox="0 0 34 34" fill="none" stroke="#fff" stroke-width="2"><path d="M8 14a9 9 0 0 1 18 0zM6 14h22M6 32c0-7 5-11 11-11s11 4 11 11"/></svg></div><b>1000 +</b><small>Expert Employee</small></div>
<div class="stat" style="left:404px"><div class="ring"><svg width="34" height="34" viewBox="0 0 34 34" fill="none" stroke="#fff" stroke-width="2"><rect x="6" y="6" width="22" height="24" rx="2"/><path d="M11 13h12M11 19h12M11 25l3 3 6-6"/></svg></div><b>1200 +</b><small>Project Completed</small></div>
<div class="stat" style="left:604px"><div class="ring"><svg width="34" height="34" viewBox="0 0 34 34" fill="none" stroke="#fff" stroke-width="2"><circle cx="17" cy="13" r="8"/><path d="M12 20l-3 11 8-4 8 4-3-11"/></svg></div><b>306 +</b><small>Award Winning</small></div>
<div class="stat" style="left:805px"><div class="ring"><svg width="34" height="34" viewBox="0 0 34 34" fill="none" stroke="#fff" stroke-width="2"><circle cx="12" cy="12" r="5"/><circle cx="23" cy="14" r="4"/><path d="M3 30c0-6 4-10 9-10s9 4 9 10M22 21c5 0 9 3 9 9"/></svg></div><b>1106 +</b><small>Happy Clients</small></div>

<!-- footer background -->
<svg class="abs" style="left:0;top:3300px" width="1200" height="339" viewBox="0 0 1200 339">
  <defs>
    <linearGradient id="foot" x1="0" y1="0" x2="0" y2="1">
      <stop offset="0" stop-color="#1a2e63"/>
      <stop offset="1" stop-color="#0e1d47"/>
    </linearGradient>
  </defs>
  <path d="M0 100 C300 40 900 40 1200 100 V339 H0 Z" fill="url(#foot)"/>
  <path d="M80 94 C160 70 220 58 260 52" stroke="#0054aa" stroke-width="5" fill="none"/>
  <path d="M940 52 C990 58 1060 70 1120 92" stroke="#0054aa" stroke-width="5" fill="none"/>
</svg>

<!-- contact -->
<div class="contact-card"></div>
<div class="contact-photo" role="img" aria-label="Two smiling workers in hard hats reviewing a tablet in a factory"></div>
<h2 class="form-title">Let’s Work Together!</h2>
<div class="field" style="top:3089px"><svg width="10" height="10" fill="none" stroke="#1f3f95" stroke-width="1.3"><circle cx="5" cy="3" r="2.3"/><path d="M1 10c0-3 2-4.5 4-4.5s4 1.5 4 4.5"/></svg>Name</div>
<div class="field" style="top:3128px"><svg width="10" height="10" fill="none" stroke="#1f3f95" stroke-width="1.3"><rect x="0.7" y="2" width="8.6" height="6.5"/><path d="M1 2.5l4 3 4-3"/></svg>Email</div>
<div class="field" style="top:3167px"><svg width="10" height="10" fill="none" stroke="#1f3f95" stroke-width="1.3"><rect x="2.5" y="0.7" width="5" height="8.6" rx="1"/></svg>Phone</div>
<div class="field" style="top:3206px;height:60px"><svg width="10" height="10" fill="none" stroke="#1f3f95" stroke-width="1.3"><path d="M1 1h8v6H4L1 9.3z"/></svg>Message</div>
<div class="btn" style="left:679px;top:3285px;width:81px;height:28px;font-size:12px;text-transform:none">Submit</div>

<!-- footer -->
<footer>
  <div class="footer-brand"><span>RIDGEWAY</span></div>
  <h3 class="f-title" style="left:371px">Conatct Info</h3>
  <svg class="abs" style="left:371px;top:3442px" width="12" height="14" fill="none" stroke="#7badd7" stroke-width="1.5"><path d="M6 13C2 8 1 6 1 5a5 5 0 0 1 10 0c0 1-1 3-5 8z"/><circle cx="6" cy="5" r="1.8"/></svg>
  <p class="f-text" style="left:393px;top:3439px">14 Harbour Lane<br>BELMONT WA 6104<br>AUSTRALIA</p>
  <svg class="abs" style="left:371px;top:3499px" width="12" height="12" fill="none" stroke="#7badd7" stroke-width="1.5"><path d="M2 1h3l1 3-2 1a7 7 0 0 0 3 3l1-2 3 1v3c-6 1-10-3-9-9z"/></svg>
  <p class="f-text" style="left:393px;top:3497px">+61-4-5550 2190</p>
  <svg class="abs" style="left:371px;top:3528px" width="13" height="10" fill="none" stroke="#7badd7" stroke-width="1.5"><rect x="1" y="1" width="11" height="8"/><path d="M1 1l5.5 4L12 1"/></svg>
  <p class="f-text" style="left:393px;top:3526px">hello@ridgewaymaint.com</p>

  <h3 class="f-title" style="left:604px">Quick Link</h3>
  <a class="f-link" style="top:3432px;color:var(--sky);text-decoration:underline">Home</a>
  <a class="f-link" style="top:3452px">About Us</a>
  <a class="f-link" style="top:3471px">What We Do</a>
  <a class="f-link" style="top:3490px">Gallery</a>
  <a class="f-link" style="top:3510px">Testimonials</a>
  <a class="f-link" style="top:3529px">Contact Us</a>

  <div class="map" role="img" aria-label="Street map showing the office location"></div>

  <div class="bottom-bar">
    <p>© 2024 Ridgeway Maintenance Services. all right reserved</p>
    <span style="left:965px;border:none;background:none"><svg width="14" height="14"><circle cx="7" cy="7" r="3" fill="#fff"/></svg></span>
    <span style="left:990px;top:8px;width:24px;height:24px;background:#fff;border:none"></span>
    <span style="left:1025px;border:none"><svg width="14" height="14"><rect x="3" y="3" width="8" height="8" fill="#fff"/></svg></span>
  </div>
</footer>

</body>
</html>
```